Business Card for Fashion House

We need a business card design for our personalize fashion service for our customers. the business card should reflect reliability, luxury and creativity.
The brand Gravetto is extracted from "Graceful Vetto"; Gravetto provides fashion designs sprinkled with luxury and style tailored for our elite clients character profile.
Gravetto is created for those who embody class and elegance with a passion for style.
Target Market(s)
Affluent Customers
Industry/Entity Type
Fashion
Contact Information for Business Card
Rania Bou Khalil
Fashion Designer
Telephone: +971 5550123
Mobile +971 555987
Emal q@z.com
Website www.gravetto-example.com
Social Media Youtube g+ Facebook Instagram Pin /gravetto
Font styles to use
Other font styles liked:
- Audrey provided
Look and feel
Each slider illustrates characteristics of the customer's brand and the style your logo design should communicate.

```html
<!DOCTYPE html>
<html lang="en">
<head>
<meta charset="utf-8">
<title>Gravetto Business Card</title>
<link href="https://fonts.googleapis.com/css2?family=Marcellus&family=Montserrat:wght@400&display=swap" rel="stylesheet">
<style>
  :root {
    --backdrop: #1a1a1a;
    --paper: #ffffff;
    --ink: #111111;
    --ink-soft: #3a3a3a;
    --card-dark: #1f1f1f;
    --card-dark-light: #363636;
    --on-dark: #ffffff;
  }
  * { box-sizing: border-box; margin: 0; padding: 0; }
  html, body { width: 1200px; height: 897px; overflow: hidden; background: var(--backdrop); }
  .canvas { position: relative; width: 1200px; height: 897px; }
  .card {
    position: absolute; left: 304px; width: 594px; height: 338px;
    border-radius: 18px; overflow: hidden;
    box-shadow: 0 6px 16px rgba(0,0,0,.45);
  }
  .card--front { top: 92px; background: var(--paper); color: var(--ink); }
  .card--back {
    top: 470px; color: var(--on-dark);
    background: linear-gradient(300deg, var(--card-dark) 20%, var(--card-dark-light) 45%, var(--card-dark) 75%);
  }
  .brand-circle { position: absolute; border-radius: 50%; border: 3px solid currentColor; }
  .card--front .brand-circle { left: 146px; top: 104px; width: 72px; height: 72px; }
  .card--back .brand-circle { left: 257px; top: 89px; width: 80px; height: 80px; }
  .wordmark {
    position: absolute; font-family: "Marcellus", serif; font-weight: 400;
    letter-spacing: 0.42em; white-space: nowrap; text-align: center;
  }
  .card--front .wordmark { left: 60px; width: 270px; top: 200px; font-size: 30px; padding-left: 0.42em; }
  .card--back .wordmark { left: 0; width: 594px; top: 209px; font-size: 34px; padding-left: 0.42em; }
  .divider { position: absolute; left: 326px; top: 102px; width: 2px; height: 134px; background: var(--ink); }
  .person { position: absolute; left: 352px; top: 96px; }
  .person__name { font-family: "Marcellus", serif; font-size: 22px; letter-spacing: 0.03em; color: var(--ink-soft); line-height: 1.1; }
  .person__role { font-family: "Montserrat", sans-serif; font-size: 14px; color: var(--ink-soft); margin-top: 4px; letter-spacing: 0.02em; }
  .contacts { position: absolute; left: 354px; top: 161px; list-style: none; }
  .contacts li {
    display: flex; align-items: center; height: 19.5px;
    font-family: "Montserrat", sans-serif; font-size: 13.5px; color: var(--ink-soft);
  }
  .contacts svg { width: 11px; height: 11px; margin-right: 12px; fill: var(--ink-soft); flex: none; }
  .social-handle {
    position: absolute; left: 0; width: 594px; top: 284px; text-align: center;
    font-family: "Montserrat", sans-serif; font-size: 20px; letter-spacing: 0.06em;
  }
</style>
</head>
<body>
<main class="canvas">
  <section class="card card--front" aria-label="Card front">
    <span class="brand-circle" aria-hidden="true"></span>
    <div class="wordmark">GRAVETTO</div>
    <span class="divider" aria-hidden="true"></span>
    <div class="person">
      <h1 class="person__name">RANIA BOU KHALIL</h1>
      <p class="person__role">Fashion Designer</p>
    </div>
    <ul class="contacts">
      <li><svg viewBox="0 0 12 12"><path d="M2.4 0.6l2 2.2-1 1.3c.7 1.5 1.9 2.7 3.5 3.5l1.3-1 2.2 2-1 2.2C5.6 10.8 1.2 6.4 0.4 1.6z"/></svg>+971 5550123</li>
      <li><svg viewBox="0 0 12 12"><path d="M3 0h6v12H3zM4 1.5v8h4v-8z"/></svg>+971 555987</li>
      <li><svg viewBox="0 0 12 12"><path d="M0 2h12v8H0zM1 3v.4l5 3.2 5-3.2V3zM1 4.6V9h10V4.6L6 7.8z"/></svg>q@z.com</li>
      <li><svg viewBox="0 0 12 12" fill="none"><g stroke="#3a3a3a" stroke-width="1" fill="none"><circle cx="6" cy="6" r="5.3"/><ellipse cx="6" cy="6" rx="2.3" ry="5.3"/><path d="M0.7 6h10.6M1.6 3.3h8.8M1.6 8.7h8.8"/></g></svg>www.gravetto-example.com</li>
    </ul>
  </section>

  <section class="card card--back" aria-label="Card back">
    <span class="brand-circle" aria-hidden="true"></span>
    <div class="wordmark">GRAVETTO</div>
    <p class="social-handle">/gravetto</p>
  </section>
</main>
</body>
</html>
```